Business Card and Letterhead for Nurlo - modern real estate business

I need a double sided business card design for Nurlo. Please see business card brief here https://papers.trelvimo.net/sheet/q/7XrTbaLeZpMmQ2uWvd9HkCj4yNoEfsGi3lRtAz_pk/view?mode=shared

Please feel free to design the business cards however you feel best. I am happy to give some creative freedoms and then provide feedback from there.

Please then also create a letterhead to match the business card design

Colors

Designer to choose colors to be used in the design.

Requirements
Must have
• Must be a modern, elegant business card which looks very professional

```html
<!DOCTYPE html>
<html lang="en">
<head>
<meta charset="utf-8">
<title>Nurlo Business Card</title>
<link href="https://fonts.googleapis.com/css2?family=Montserrat:wght@400;500;600&display=swap" rel="stylesheet">
<style>
  :root {
    --stage: #1c1c1c;
    --card-black: #050304;
    --stripe: #2a2728;
    --red: #e31e26;
    --ink: #1a1a1a;
    --white: #ffffff;
    --rule: #333333;
  }
  * { margin: 0; padding: 0; box-sizing: border-box; }
  html, body {
    width: 1200px; height: 900px; overflow: hidden;
    background: var(--stage);
    font-family: "Montserrat", Arial, sans-serif;
  }
  .canvas { position: relative; width: 1200px; height: 900px; }
  .card {
    position: absolute; left: 250px; width: 700px; height: 380px; overflow: hidden;
  }
  /* Front */
  .card-front { top: 50px; background: var(--card-black); }
  .card-front .stripes { position: absolute; inset: 0; }
  .brand-name {
    position: absolute; left: 0; right: 0; top: 118px; text-align: center;
    font-weight: 600; font-size: 96px; letter-spacing: 6px; color: var(--red);
    line-height: 1;
  }
  .front-url {
    position: absolute; left: 0; right: 0; top: 318px; text-align: center;
    font-size: 15px; letter-spacing: 1.5px; color: var(--white);
  }
  .front-url strong { color: var(--red); font-weight: 600; }
  /* Back */
  .card-back { top: 470px; background: var(--white); }
  .photo-frame {
    position: absolute; left: 150px; top: 96px; width: 174px; height: 182px;
    border: 1.5px solid var(--red);
  }
  .portrait {
    position: absolute; left: 160px; top: 106px; width: 154px; height: 162px;
    border: 3px solid var(--ink);
    background: linear-gradient(160deg, #9fb39a 0%, #6f7d62 45%, #2b2a2c 75%, #1d1d20 100%);
  }
  .divider {
    position: absolute; left: 352px; top: 104px; width: 2px; height: 176px;
    background: var(--rule);
  }
  .details { position: absolute; left: 376px; top: 100px; color: var(--ink); }
  .agent-name {
    font-weight: 600; font-size: 27px; letter-spacing: 2px; color: var(--red);
    text-transform: uppercase; line-height: 1.05;
  }
  .agent-role { font-size: 15px; margin-top: 2px; letter-spacing: 0.5px; }
  .address { font-size: 15px; margin-top: 14px; line-height: 1.3; letter-spacing: 1px; }
  .contacts { list-style: none; margin-top: 12px; font-size: 16px; letter-spacing: 1px; }
  .contacts li { display: flex; align-items: center; gap: 12px; line-height: 1.5; }
  .contacts svg { width: 14px; height: 14px; flex: none; }
  .bottom-band {
    position: absolute; left: 430px; right: 0; bottom: 0; height: 14px; background: var(--red);
  }
</style>
</head>
<body>
<main class="canvas">
  <section class="card card-front">
    <svg class="stripes" viewBox="0 0 700 380" aria-hidden="true">
      <polygon points="150,0 172,0 268,150 250,150" fill="var(--stripe)"/>
      <polygon points="225,0 247,0 343,150 325,150" fill="var(--stripe)"/>
      <polygon points="190,175 212,175 22,380 0,380" fill="var(--stripe)"/>
    </svg>
    <div class="brand-name">NURLO</div>
    <div class="front-url">www.<strong>nurlo</strong>.com</div>
  </section>

  <section class="card card-back">
    <div class="photo-frame"></div>
    <div class="portrait" role="img" aria-label="Portrait photo of the agent outdoors"></div>
    <div class="divider"></div>
    <div class="details">
      <h1 class="agent-name">Liam Carter</h1>
      <p class="agent-role">Licenced Real Estate Agent</p>
      <p class="address">PO Box 3170<br>Larkfield NSW 2790</p>
      <ul class="contacts">
        <li>
          <svg viewBox="0 0 24 24"><path fill="var(--red)" d="M6.6 10.8a15.1 15.1 0 006.6 6.6l2.2-2.2c.3-.3.7-.4 1-.2 1.1.4 2.3.6 3.6.6.6 0 1 .4 1 1V20c0 .6-.4 1-1 1A17 17 0 013 4c0-.6.4-1 1-1h3.5c.6 0 1 .4 1 1 0 1.3.2 2.5.6 3.6.1.3 0 .7-.2 1z"/></svg>
          0400 381 592
        </li>
        <li>
          <svg viewBox="0 0 24 24" fill="none" stroke="var(--red)" stroke-width="2"><rect x="2" y="5" width="20" height="14"/><path d="M2 5l10 8 10-8"/></svg>
          liam@nurlo.com
        </li>
        <li>
          <svg viewBox="0 0 24 24" fill="none" stroke="var(--red)" stroke-width="1.8"><circle cx="12" cy="12" r="10"/><path d="M2 12h20M12 2c3 3 3 17 0 20M12 2c-3 3-3 17 0 20"/></svg>
          www.nurlo.com
        </li>
      </ul>
    </div>
    <div class="bottom-band"></div>
  </section>
</main>
</body>
</html>
```